Fitness Equipment & Service

I want to make the card eye catching and fun. We are called Copperleaf Motion Limited and we are based in Wales. We sell, install and service all types of fitness equipment from Skipping ropes, right through the Dumbbells, Kettle bells and Barbells through to state of the art Treadmills, Running Machines and Strength Equipment. We also design and install changing room furniture and lockers.

TYPOGRAPHY
We would like to use Futrura. Futura has an appearance of efficiency and forwardness. The typeface is derived
from simple geometric forms (near-perfect circles, triangles and squares) and is based on strokes of
near-even weight, which are low in contrast. This is most visible in the almost perfectly round stroke of
the o, which is nonetheless slightly ovoid.
The lowercase has tall ascenders, which rise above the cap line. The uppercase
characters present proportions similar to those of classical Roman capitals.

TYPOGRAPHIC CONSIDERATIONS
No Strike though
No Horizontal Scaling
No Drop Shadows
No Effects
Never use less than 120% Leading

OUR CORPORATE COLOURS
BRAND GUIDELINES
We were thinking that our primary colour palette consists of the Acid Green (Pantone 382) and Process Black.

We work closely with torvane Ltd and would like to include their name on the card somewhere. I have attached images of the other brands that we work with as an idea or the small icons I have included that illustrate what we do?. I have very kindly been given permission to use any of the images off the files that I have included below, so I hope these help. I will include these below. I would be open to suggestions if it made the card more striking Can you do it?

Hi All, Just wanted to add a few thoughts but you are the guys with the creative visions (thats why are here) We are based in Wales, UK and we would be open to lots of different ideas on a theme but must be eye catching, Bold and FUN. If you can or think that the Welsh or any dragon could be put in there then go for it (its not a must have) We have also added some ideas for colour but again its over to you!! GO FOR IT ! Thanks and look forward to your visions! Owen

Hi All, Just thought I would sen through the contact details that need to be on the card. (if you want to play around with icons instead of the wording twitter, Facebook, go for it): Copperleaf Motion Limited Owen Pritchard Managing Director Mob: +44 (0)7391 508 262 e-mail: sales@copperleafmotion.co.uk Web: Copperleafmotion.co.uk twitter: @motionParcelbin Facebook: Copperleaf Motion Limited

```html
<!DOCTYPE html>
<html lang="en">
<head>
<meta charset="utf-8">
<title>Copperleaf Motion Limited — Business Card Options</title>
<link href="https://fonts.googleapis.com/css2?family=Lato:wght@400;700&display=swap" rel="stylesheet">
<style>
  :root {
    --stage-top: #2e2e2e;
    --stage-bottom: #6b6b6b;
    --acid-green: #72b33e;
    --green-text: #8cc84b;
    --card-black: #161616;
    --navy: #1c2638;
    --rule-grey: #7a7a7a;
    --white: #ffffff;
    --tile-blue: #2f8fd6;
    --badge-grey: #3a3a3a;
    --label-grey: #e6e6e6;
  }
  * { box-sizing: border-box; margin: 0; padding: 0; }
  html, body { width: 1200px; height: 541px; overflow: hidden; }
  body {
    font-family: "Lato", Arial, sans-serif;
    background: linear-gradient(180deg, var(--stage-top), var(--stage-bottom));
    position: relative;
  }
  .icon-library { position: absolute; width: 0; height: 0; }
  .card { position: absolute; overflow: hidden; }
  .card-front { top: 26px; width: 387px; height: 232px; }
  .card-back { top: 270px; width: 385px; height: 228px;
    background: radial-gradient(ellipse at 40% 40%, #2e2e2e, var(--card-black) 75%); }
  .option-a { left: 10px; } .option-b { left: 404px; } .option-c { left: 802px; }
  .back-a { left: 16px; } .back-b { left: 410px; } .back-c { left: 803px; }
  .card svg.shapes { position: absolute; inset: 0; }
  .gym-icon { color: var(--white); }
  .text { position: absolute; color: var(--white); line-height: 1.2; white-space: nowrap; }
  .partner-name { left: 34px; top: 12px; font-size: 10px; font-weight: 700; color: var(--navy); }
  .person-name { right: 36px; top: 44px; font-size: 12.5px; font-weight: 700; }
  .person-role { right: 36px; top: 59px; font-size: 10px; color: var(--green-text); }
  .option-c .person-name, .option-c .person-role { right: 42px; }
  .brand-name { left: 72px; top: 82px; font-size: 11.5px; font-weight: 700; color: var(--navy); line-height: 1.2; }
  .social-handle { left: 72px; top: 147px; font-size: 9.5px; }
  .social-page { left: 18px; top: 179px; font-size: 9px; }
  .contact { right: 33px; text-align: right; font-size: 9.5px; }
  .option-c .contact { right: 34px; }
  .contact-phone { top: 141px; } .contact-email { top: 176px; }
  .back-brand { left: 0; right: 0; top: 190px; text-align: center; font-size: 12px; letter-spacing: 0.5px; color: var(--label-grey); }
  .option-letter { position: absolute; top: 476px; font-size: 34px; color: #e8e8e8; font-weight: 400; }
</style>
</head>
<body>

<svg class="icon-library" aria-hidden="true">
  <defs>
    <linearGradient id="cardBlack" x1="0" y1="0" x2="1" y2="1"><stop offset="0" stop-color="#2e2e2e"/><stop offset="1" stop-color="#121212"/></linearGradient>
    <symbol id="icon-dumbbell" viewBox="0 0 24 24"><g fill="currentColor"><rect x="2" y="8" width="4" height="8" rx="1"/><rect x="18" y="8" width="4" height="8" rx="1"/><rect x="6" y="11" width="12" height="2"/></g></symbol>
    <symbol id="icon-kettlebell" viewBox="0 0 24 24"><circle cx="12" cy="15" r="7" fill="currentColor"/><path d="M7 10 V6 a2 2 0 0 1 2 -2 h6 a2 2 0 0 1 2 2 V10" fill="none" stroke="currentColor" stroke-width="2.2"/></symbol>
    <symbol id="icon-bike" viewBox="0 0 24 24"><g fill="none" stroke="currentColor" stroke-width="1.8"><circle cx="7" cy="17" r="4"/><circle cx="18" cy="17" r="3"/><path d="M7 17 L11 7 L17 7 M11 7 L18 17 M9 5 h5"/></g></symbol>
    <symbol id="icon-scale" viewBox="0 0 24 24"><rect x="3" y="3" width="18" height="18" rx="4" fill="currentColor"/><circle cx="12" cy="10" r="4" fill="#1a1a1a"/><line x1="12" y1="10" x2="14" y2="8" stroke="currentColor" stroke-width="1.2"/></symbol>
    <symbol id="icon-treadmill" viewBox="0 0 24 24"><g fill="currentColor"><rect x="1" y="16" width="22" height="3" rx="1"/><rect x="2" y="20" width="20" height="1.4"/><rect x="3" y="6" width="18" height="1.6"/><rect x="3" y="10" width="12" height="1.6"/></g></symbol>
    <symbol id="icon-glove" viewBox="0 0 24 24"><path d="M6 4 h9 a5 5 0 0 1 5 5 v5 a4 4 0 0 1 -4 4 h-1 v3 h-8 v-5 a4 4 0 0 1 -3 -4 v-4 a4 4 0 0 1 2 -4z" fill="currentColor"/><line x1="7" y1="16" x2="15" y2="16" stroke="#1a1a1a" stroke-width="1.2"/></symbol>
    <symbol id="icon-apple" viewBox="0 0 24 24"><path d="M12 8 c-3 -2 -8 -1 -8 5 c0 5 4 9 6 9 c1 0 1.5 -0.6 2 -0.6 s1 0.6 2 0.6 c2 0 6 -4 6 -9 c0 -6 -5 -7 -8 -5z" fill="currentColor"/><path d="M12 8 q0 -3 3 -5" fill="none" stroke="currentColor" stroke-width="1.6"/></symbol>
    <symbol id="icon-rope" viewBox="0 0 24 24"><path d="M4 20 Q4 4 12 4 Q20 4 20 20" fill="none" stroke="currentColor" stroke-width="1.4" stroke-dasharray="2 1.6"/><g fill="currentColor"><rect x="2.5" y="17" width="3" height="6" rx="1.2"/><rect x="18.5" y="17" width="3" height="6" rx="1.2"/></g></symbol>
    <symbol id="icon-locker" viewBox="0 0 24 24"><rect x="4" y="2" width="16" height="20" rx="2" fill="currentColor"/><g stroke="#1a1a1a" stroke-width="1.3"><line x1="7" y1="6" x2="17" y2="6"/><line x1="7" y1="9" x2="17" y2="9"/><line x1="7" y1="14" x2="17" y2="14"/></g></symbol>
    <symbol id="icon-bench" viewBox="0 0 24 24"><g fill="none" stroke="currentColor" stroke-width="2" stroke-linecap="round"><path d="M3 14 L15 14 L21 6"/><path d="M6 14 V20 M14 14 V20"/></g><circle cx="19" cy="16" r="2" fill="currentColor"/></symbol>
  </defs>
</svg>

<!-- Option A front -->
<div class="card card-front option-a">
  <svg class="shapes" viewBox="0 0 387 232" width="387" height="232">
    <rect width="387" height="232" fill="url(#cardBlack)"/>
    <g class="gym-icon" role="img" aria-label="Scattered white icons of gym equipment">
      <use href="#icon-glove" x="190" y="8" width="22" height="22"/>
      <use href="#icon-locker" x="222" y="8" width="22" height="22"/>
      <use href="#icon-bike" x="252" y="8" width="24" height="24"/>
      <use href="#icon-apple" x="285" y="12" width="20" height="20"/>
      <use href="#icon-treadmill" x="320" y="6" width="24" height="20"/>
      <use href="#icon-rope" x="352" y="4" width="24" height="24"/>
      <use href="#icon-scale" x="208" y="42" width="22" height="22"/>
      <use href="#icon-kettlebell" x="234" y="42" width="20" height="20"/>
      <use href="#icon-rope" x="256" y="46" width="16" height="16"/>
      <use href="#icon-scale" x="358" y="44" width="22" height="22"/>
      <use href="#icon-apple" x="222" y="78" width="20" height="20"/>
      <use href="#icon-treadmill" x="246" y="76" width="26" height="20"/>
      <use href="#icon-dumbbell" x="286" y="72" width="24" height="24"/>
      <use href="#icon-apple" x="322" y="76" width="22" height="22"/>
      <use href="#icon-glove" x="356" y="74" width="24" height="24"/>
      <use href="#icon-bench" x="228" y="104" width="24" height="22"/>
      <use href="#icon-scale" x="262" y="106" width="18" height="18"/>
      <use href="#icon-bench" x="286" y="100" width="24" height="22"/>
      <use href="#icon-treadmill" x="318" y="104" width="24" height="18"/>
      <use href="#icon-bike" x="354" y="102" width="24" height="24"/>
    </g>
    <polygon points="0,0 170,0 212,110 168,232 0,232" fill="var(--acid-green)"/>
    <polygon points="170,0 186,0 228,110 212,110" fill="var(--white)"/>
    <g fill="var(--badge-grey)"><rect x="92" y="11" width="58" height="12" rx="2"/><rect x="10" y="31" width="55" height="12" rx="2"/><rect x="68" y="31" width="52" height="12" rx="6"/><rect x="123" y="31" width="52" height="12" rx="2"/></g>
    <circle cx="42" cy="102" r="25" fill="var(--navy)" stroke="var(--white)" stroke-width="2.5"/>
    <line x1="18" y1="171" x2="370" y2="171" stroke="var(--rule-grey)" stroke-width="0.8"/>
    <g fill="var(--white)"><polygon points="154,138 188,138 181,169 147,169"/><polygon points="192,138 226,138 219,169 185,169"/><polygon points="146,174 180,174 173,206 139,206"/><polygon points="184,174 218,174 211,206 177,206"/></g>
    <circle cx="168" cy="153" r="7" fill="var(--tile-blue)"/>
    <path d="M200 148 q4 -3 8 0 l-1.5 3 h-5 z M199 151 h10 v8 h-10 z" fill="var(--acid-green)"/>
    <rect x="153" y="183" width="13" height="13" fill="var(--tile-blue)"/>
    <g fill="none" stroke="var(--acid-green)" stroke-width="1.8"><rect x="190" y="182" width="14" height="10"/><line x1="197" y1="192" x2="197" y2="197"/><line x1="193" y1="197" x2="201" y2="197"/></g>
  </svg>
  <div class="text partner-name">torvane</div>
  <div class="text person-name">Owen Pritchard</div>
  <div class="text person-role">Managing Director</div>
  <div class="text brand-name">Copperleaf<br>Motion<br>Limited</div>
  <div class="text social-handle">@motionParcelbin</div>
  <div class="text social-page">Copperleaf Motion Limited</div>
  <div class="text contact contact-phone">+44 (0)7391 508 262<br>000 . 0000 . 0000</div>
  <div class="text contact contact-email">sales@copperleafmotion.co.uk<br>Copperleafmotion.co.uk</div>
</div>

<!-- Option B front -->
<div class="card card-front option-b">
  <svg class="shapes" viewBox="0 0 387 232" width="387" height="232">
    <rect width="387" height="232" fill="url(#cardBlack)"/>
    <g class="gym-icon" role="img" aria-label="Cluster of white gym equipment icons near the top">
      <use href="#icon-scale" x="194" y="6" width="22" height="22"/>
      <use href="#icon-glove" x="226" y="8" width="22" height="22"/>
      <use href="#icon-bike" x="258" y="6" width="26" height="26"/>
      <use href="#icon-bench" x="206" y="40" width="26" height="24"/>
      <use href="#icon-kettlebell" x="242" y="40" width="22" height="22"/>
      <use href="#icon-glove" x="222" y="72" width="18" height="18"/>
      <use href="#icon-apple" x="230" y="84" width="20" height="20"/>
    </g>
    <g class="gym-icon" role="img" aria-label="White icons of a locker, treadmill and skipping rope in the lower corner">
      <use href="#icon-locker" x="352" y="148" width="24" height="26"/>
      <use href="#icon-treadmill" x="316" y="202" width="30" height="20"/>
      <use href="#icon-rope" x="352" y="198" width="24" height="24"/>
    </g>
    <polygon points="0,0 170,0 212,110 168,232 0,232" fill="var(--acid-green)"/>
    <polygon points="170,0 186,0 228,110 212,110" fill="var(--white)"/>
    <g fill="var(--badge-grey)"><rect x="92" y="11" width="58" height="12" rx="2"/><rect x="10" y="31" width="55" height="12" rx="2"/><rect x="68" y="31" width="52" height="12" rx="6"/><rect x="123" y="31" width="52" height="12" rx="2"/></g>
    <circle cx="42" cy="102" r="25" fill="var(--navy)" stroke="var(--white)" stroke-width="2.5"/>
    <line x1="18" y1="171" x2="345" y2="171" stroke="var(--rule-grey)" stroke-width="0.8"/>
    <g fill="var(--white)"><polygon points="154,138 188,138 181,169 147,169"/><polygon points="192,138 226,138 219,169 185,169"/><polygon points="146,174 180,174 173,206 139,206"/><polygon points="184,174 218,174 211,206 177,206"/></g>
    <circle cx="168" cy="153" r="7" fill="var(--tile-blue)"/>
    <path d="M200 148 q4 -3 8 0 l-1.5 3 h-5 z M199 151 h10 v8 h-10 z" fill="var(--acid-green)"/>
    <rect x="153" y="183" width="13" height="13" fill="var(--tile-blue)"/>
    <g fill="none" stroke="var(--acid-green)" stroke-width="1.8"><rect x="190" y="182" width="14" height="10"/><line x1="197" y1="192" x2="197" y2="197"/><line x1="193" y1="197" x2="201" y2="197"/></g>
  </svg>
  <div class="text partner-name">torvane</div>
  <div class="text person-name">Owen Pritchard</div>
  <div class="text person-role">Managing Director</div>
  <div class="text brand-name">Copperleaf<br>Motion<br>Limited</div>
  <div class="text social-handle">@motionParcelbin</div>
  <div class="text social-page">Copperleaf Motion Limited</div>
  <div class="text contact contact-phone">+44 (0)7391 508 262<br>000 . 0000 . 0000</div>
  <div class="text contact contact-email">sales@copperleafmotion.co.uk<br>Copperleafmotion.co.uk</div>
</div>

<!-- Option C front -->
<div class="card card-front option-c">
  <svg class="shapes" viewBox="0 0 387 232" width="387" height="232">
    <rect width="387" height="232" fill="url(#cardBlack)"/>
    <g class="gym-icon" role="img" aria-label="Column of white gym equipment icons along the right edge">
      <use href="#icon-scale" x="362" y="40" width="20" height="20"/>
      <use href="#icon-glove" x="360" y="68" width="22" height="22"/>
      <use href="#icon-bike" x="358" y="98" width="24" height="24"/>
      <use href="#icon-rope" x="362" y="150" width="18" height="18"/>
      <use href="#icon-kettlebell" x="362" y="174" width="20" height="20"/>
      <use href="#icon-locker" x="360" y="200" width="22" height="24"/>
      <use href="#icon-bench" x="288" y="104" width="26" height="24"/>
      <use href="#icon-apple" x="326" y="92" width="22" height="22"/>
      <use href="#icon-treadmill" x="318" y="118" width="26" height="16"/>
    </g>
    <polygon points="0,0 170,0 212,110 168,232 0,232" fill="var(--acid-green)"/>
    <polygon points="170,0 186,0 228,110 212,110" fill="var(--white)"/>
    <g fill="var(--badge-grey)"><rect x="92" y="11" width="58" height="12" rx="2"/><rect x="10" y="31" width="55" height="12" rx="2"/><rect x="68" y="31" width="52" height="12" rx="6"/><rect x="123" y="31" width="52" height="12" rx="2"/></g>
    <circle cx="42" cy="102" r="25" fill="var(--navy)" stroke="var(--white)" stroke-width="2.5"/>
    <line x1="18" y1="171" x2="352" y2="171" stroke="var(--rule-grey)" stroke-width="0.8"/>
    <g fill="var(--white)"><polygon points="154,138 188,138 181,169 147,169"/><polygon points="192,138 226,138 219,169 185,169"/><polygon points="146,174 180,174 173,206 139,206"/><polygon points="184,174 218,174 211,206 177,206"/></g>
    <circle cx="168" cy="153" r="7" fill="var(--tile-blue)"/>
    <path d="M200 148 q4 -3 8 0 l-1.5 3 h-5 z M199 151 h10 v8 h-10 z" fill="var(--acid-green)"/>
    <rect x="153" y="183" width="13" height="13" fill="var(--tile-blue)"/>
    <g fill="none" stroke="var(--acid-green)" stroke-width="1.8"><rect x="190" y="182" width="14" height="10"/><line x1="197" y1="192" x2="197" y2="197"/><line x1="193" y1="197" x2="201" y2="197"/></g>
  </svg>
  <div class="text partner-name">torvane</div>
  <div class="text person-name">Owen Pritchard</div>
  <div class="text person-role">Managing Director</div>
  <div class="text brand-name">Copperleaf<br>Motion<br>Limited</div>
  <div class="text social-handle">@motionParcelbin</div>
  <div class="text social-page">Copperleaf Motion Limited</div>
  <div class="text contact contact-phone">+44 (0)7391 508 262<br>000 . 0000 . 0000</div>
  <div class="text contact contact-email">sales@copperleafmotion.co.uk<br>Copperleafmotion.co.uk</div>
</div>

<!-- Backs -->
<div class="card card-back back-a">
  <svg class="shapes" viewBox="0 0 385 228" width="385" height="228"><circle cx="193" cy="94" r="66" fill="var(--navy)" stroke="var(--white)" stroke-width="5"/></svg>
  <div class="text back-brand">COPPERLEAF MOTION LIMITED</div>
</div>
<div class="card card-back back-b">
  <svg class="shapes" viewBox="0 0 385 228" width="385" height="228"><circle cx="193" cy="94" r="66" fill="var(--navy)" stroke="var(--white)" stroke-width="5"/></svg>
  <div class="text back-brand">COPPERLEAF MOTION LIMITED</div>
</div>
<div class="card card-back back-c">
  <svg class="shapes" viewBox="0 0 385 228" width="385" height="228"><circle cx="193" cy="94" r="66" fill="var(--navy)" stroke="var(--white)" stroke-width="5"/></svg>
  <div class="text back-brand">COPPERLEAF MOTION LIMITED</div>
</div>

<div class="option-letter" style="left:18px">A</div>
<div class="option-letter" style="left:414px">B</div>
<div class="option-letter" style="left:808px">C</div>

</body>
</html>
```